Company brochure for our unique consulting business

We are a small consulting business offering a unique set of services to our clients.. In simple terms we are a business improvement consultancy helping our clients get the best out of their businesses. We work with clients across multiple sectors and deliver a variety of services. We want to put together a brochure to cover these main themes:1. Who we are2. What we do3. The type of people we employ4. The sectors we work inWhile the brochure needs to have a certain corporate feel to it, we don't want it to be "boring" or "stiff". We would like it to have a slightly "friendly" or "informal" feel to it, to reflect the type of organisation we are.We have a company website http://kellbrookadvisory.example , however we do not want to directly replicate the content or feel as we recognise it needs updating.We would like the brochure to be A4 portrait format. We anticipate requiring 12 sides (including covers) but we are happy to be guided on this based on the content we have provided.The attached ppt file gives the detail of the content to be included and also shows the proposed pagination. For the front cover we would like to try 2 versions, one with the KBA logo and one with the Kellbrook Advisory logo (a file of both is attached)One of the most important pages will be the "Our Services" page. We would like this to cover the centre fold. In the ppt file we have shown an example layout, but this is where we need most help - we are clearly not graphic designers! This page will be the most used page in sales meetings etc.Also attached is the following:1. file for our KellBrook Advisory company logo.2. File for our KBA company logo3. Files for Derek's signatures (for under photos) - Owen's to follow4. Photo of Derek & Owen (person in purple shirt to be cropped out)Thank you and really excited to see what everyone comes back with.Derek & Owen

Target Market(s)

Very broad - Manufacturing, Healthcare, Hospitality

Industry/Entity Type

Management Consulting

Font styles to use
Other font styles liked:
• We use Swiss721, but happy to be guided by designer

Colors
3276b5
85abd2
0355a3
333333
5c5c5c
9d9d9d
d9d9d9

Requirements
Must have
• Corporate feel
Nice to have
• Slightly friendly feel
• Our standard "blue" is (CORRECTION) - R55 G96 B146 #376092 and our standard grey is R197 G178, B179 - #B3B2B2, which we would like to keep, but other colours we are happy to be guided on. Brand guidelines attached.

```html
<!DOCTYPE html>
<html lang="en">
<head>
<meta charset="utf-8">
<title>Kellbrook Advisory – Our People &amp; Quotes</title>
<link href="https://fonts.googleapis.com/css2?family=Arimo:ital,wght@0,400;0,700;1,400&family=Open+Sans:wght@800&display=swap" rel="stylesheet">
<style>
  :root{
    --blue-deep:#0355a3;
    --blue-mid:#3276b5;
    --blue-soft:#85abd2;
    --ink:#333333;
    --text:#5c5c5c;
    --muted:#9d9d9d;
    --rule:#d9d9d9;
    --paper:#ffffff;
    --backdrop:#ececec;
  }
  *{box-sizing:border-box;margin:0;padding:0}
  html,body{width:1200px;height:840px;overflow:hidden;background:var(--backdrop)}
  body{font-family:"Arimo",Arial,sans-serif;color:var(--text)}
  .spread{position:absolute;left:60px;top:40px;width:1080px;height:760px;display:flex;box-shadow:0 6px 24px rgba(0,0,0,.12)}
  .page{position:relative;width:540px;height:760px;background:var(--paper);overflow:hidden}
  .page--left{background:linear-gradient(to left,rgba(0,0,0,.07),rgba(0,0,0,0) 40px),var(--paper)}
  .page--right{background:linear-gradient(to right,rgba(0,0,0,.07),rgba(0,0,0,0) 40px),var(--paper)}

  /* Left page */
  .section-title{position:absolute;left:46px;top:60px;display:flex;align-items:stretch;font-size:15px;letter-spacing:.5px;text-transform:uppercase}
  .section-title__plain{padding:2px 6px;border-left:2px solid var(--blue-deep);border-bottom:1px solid var(--blue-deep);color:var(--blue-deep)}
  .section-title__accent{padding:2px 6px;background:var(--blue-deep);color:#fff;font-weight:700}
  .section-title__rule{width:60px;border-bottom:1px solid var(--blue-deep)}
  .team-photo{position:absolute;left:23px;top:104px;width:517px;height:188px;background:linear-gradient(100deg,#3a3a3a 0%,#9a9a9a 30%,#e4e4e4 55%,#bdbdbd 75%,#4a4a4a 100%)}
  .people-copy{position:absolute;left:46px;top:318px;width:450px;font-size:11px;line-height:16px}
  .people-copy p{margin-bottom:14px}
  .people-point{position:relative;padding-left:22px}
  .people-point::before{content:"";position:absolute;left:4px;top:4px;width:7px;height:7px;background:var(--blue-mid)}
  .people-point--highlight{color:var(--blue-mid);font-style:italic}
  .band--left{position:absolute;left:0;top:542px;width:540px;height:78px;background:linear-gradient(to right,var(--blue-mid),var(--blue-deep))}
  .footer-rule{position:absolute;left:46px;right:46px;top:716px;border-top:1px solid var(--rule)}
  .brand-name{position:absolute;left:46px;top:726px;display:flex;align-items:center;gap:6px;font-size:16px;font-weight:700;color:var(--blue-deep)}
  .brand-name__mark{width:10px;height:10px;background:var(--blue-deep)}

  /* Right page */
  .page-tab{position:absolute;left:46px;top:0;width:17px;height:104px;background:var(--blue-deep)}
  .quotes-title{position:absolute;left:78px;top:66px;font-family:"Open Sans",Arial,sans-serif;font-weight:800;font-size:26px;color:var(--blue-deep);letter-spacing:.5px}
  .quotes-frame{position:absolute;left:46px;top:104px;width:452px;height:545px;border:2px solid var(--blue-deep)}
  .band--right{position:absolute;left:498px;top:536px;width:42px;height:86px;background:var(--blue-deep)}
  .quote-mark{position:absolute;left:245px;width:50px;height:36px;background:var(--paper);display:flex;justify-content:center;align-items:center}
  .quote-mark--open{top:86px}
  .quote-mark--close{top:631px}
  .quote-list{position:absolute;left:76px;top:160px;width:400px;list-style:none;font-size:11px;line-height:15px}
  .quote{position:absolute;left:0;width:400px}
  .quote__source{display:block;margin-top:4px;padding-left:10px;color:var(--blue-mid)}
  .page-number{position:absolute;right:46px;top:716px;display:flex;align-items:center;gap:8px;font-size:13px;color:var(--blue-deep)}
  .page-number__mark{width:8px;height:8px;background:var(--blue-deep)}
  .footer-rule--right{left:46px;right:46px;top:740px}
</style>
</head>
<body>
<main class="spread">
  <section class="page page--left">
    <h2 class="section-title"><span class="section-title__plain">Our</span><span class="section-title__accent">People</span><span class="section-title__rule"></span></h2>
    <div class="team-photo" role="img" aria-label="Black and white photo of a consultant presenting at a flipchart to a seated team in a bright meeting room"></div>
    <div class="people-copy">
      <p>All of our team at KBA started their careers in operational roles. This means we understand what it's like to be in your shoes. Blending this understanding with our years of experience and skills we are able to work in partnership with you and your teams to deliver great results, together. Simply put, our team has some of the best people in the industry.</p>
      <p class="people-point people-point--highlight">We also recognise no single person knows everything, so within the team we have experts in their own fields. They are able to bring their specialised skills and experience, at the right time and in the best way possible.</p>
      <p class="people-point">Our team also understand the importance of engagement. Everyone in your team will get to know us on first name terms, because we take the time to listen to everyone, from shop floor to senior management.</p>
    </div>
    <div class="band--left"></div>
    <div class="footer-rule"></div>
    <div class="brand-name"><span class="brand-name__mark"></span>KBA</div>
  </section>

  <section class="page page--right">
    <div class="page-tab"></div>
    <h2 class="quotes-title">QUOTES</h2>
    <div class="band--right"></div>
    <div class="quotes-frame"></div>
    <div class="quote-mark quote-mark--open">
      <svg width="40" height="30" viewBox="0 0 40 30" aria-hidden="true"><g fill="var(--blue-deep)"><path d="M2 30V18C2 9 7 3 16 1l1 4c-5 2-7 5-7 9h7v16z"/><path d="M22 30V18c0-9 5-15 14-17l1 4c-5 2-7 5-7 9h7v16z"/></g></svg>
    </div>
    <ul class="quote-list">
      <li class="quote" style="top:0">KBA have achieved excellent engagement throughout the entire organisation with significant measurable successes<span class="quote__source">-Director of Operations<br>Norbury Group</span></li>
      <li class="quote" style="top:100px">With the team from KBA we have been able to embed an improvement approach across the entire organisation.<span class="quote__source">-Chief Operations Officer<br>Westfield Hospital</span></li>
      <li class="quote" style="top:194px">You have definitely made our lives easier knowing that you are taking care of our British colleagues. If we have future needs, we will definitely be straight back to you.<span class="quote__source">-Chief Operations Officer<br>Veterans Games Trust</span></li>
      <li class="quote" style="top:287px">The team from KBA have been invaluable with helping implement our lean programme. They've helped break down what seemed very complicated at the start, into logical and simple steps.<span class="quote__source">-Managing Director<br>Penmore Supplies</span></li>
      <li class="quote" style="top:402px">KBA have been able offer us support across a range of topics based on their in-depth knowledge of lean and Harumi systems<span class="quote__source">-Continuous Improvement Manager<br>Halvorsen Motors</span></li>
    </ul>
    <div class="quote-mark quote-mark--close">
      <svg width="40" height="30" viewBox="0 0 40 30" aria-hidden="true"><g fill="var(--blue-deep)" transform="rotate(180 20 15)"><path d="M2 30V18C2 9 7 3 16 1l1 4c-5 2-7 5-7 9h7v16z"/><path d="M22 30V18c0-9 5-15 14-17l1 4c-5 2-7 5-7 9h7v16z"/></g></svg>
    </div>
    <div class="page-number"><span class="page-number__mark"></span>5</div>
    <div class="footer-rule footer-rule--right"></div>
  </section>
</main>
</body>
</html>
```